Rock, Paper Scissors Championship Flyer

We need a dynamic, bold and exciting flyer to promote the following event at our sports center. The event will be primarily focused for adults, but children are welcome to join

Rock, Paper, Scissors Championship - $$$ prizes
Date: June 9th, 2018
Time: 11am-4pm
Fee: $2 to enter, free for spectators
Heats to determine the overall ‘Rock, Paper, Scissors’ champion!
- Cash prizes on offer
- Live music.
- Food and beverage available for purchase

Belvorrow Sports Center, Calder Falls
908-555-3162
www.belvorrowgrounds.example

Must include our logo (does not have to be huge) and County seal (both attached)

Colors

Designer to choose colors to be used in the design.

Requirements
Must have
• Should be fun and colorful
• The following info and attached logos:
• Rock, Paper, Scissors Championship - $$$ prizes
• Date: June 9th, 2018
• Time: 11am-4pm
• Fee: $2 to enter, free for spectators
• Heats to determine the overall ‘Rock, Paper, Scissors’ champion!
• - Cash prizes on offer
• - Live music.
• - Food and beverage available for purchase
• Belvorrow Sports Center, Calder Falls
• 908-555-3162
• www.belvorrowgrounds.example
Nice to have
• There are a few inspirational photos attached to give an idea of what we are looking for.

```html
<!DOCTYPE html>
<html lang="en">
<head>
<meta charset="utf-8">
<title>Rock, Paper, Scissors Championship</title>
<link href="https://fonts.googleapis.com/css2?family=Anton&family=Montserrat:wght@400;600;700;800&display=swap" rel="stylesheet">
<style>
  :root {
    --page-bg: #b3b1bb;
    --navy: #1c1256;
    --navy-deep: #110a36;
    --violet: #2e1f7a;
    --yellow: #ffd400;
    --magenta: #b84fb0;
    --cyan: #5ec8e0;
    --photo-blue: #5aaec6;
    --white: #ffffff;
  }
  * { margin: 0; padding: 0; box-sizing: border-box; }
  html, body { width: 1200px; height: 893px; overflow: hidden; }
  body {
    background: var(--page-bg);
    font-family: "Montserrat", sans-serif;
    position: relative;
  }
  .flyer {
    position: absolute;
    left: 300px; top: 21px;
    width: 600px; height: 850px;
    background: radial-gradient(ellipse at 50% 45%, var(--violet) 0%, var(--navy) 55%, var(--navy-deep) 100%);
    overflow: hidden;
    color: var(--white);
  }
  .decor { position: absolute; inset: 0; }
  .title-box {
    position: absolute;
    left: 95px; top: 300px;
    width: 410px; height: 175px;
    background: var(--yellow);
    transform: rotate(-6deg);
    box-shadow: 0 0 24px rgba(255, 212, 0, 0.55);
    text-align: center;
    font-family: "Anton", sans-serif;
    color: var(--navy);
    text-transform: uppercase;
    line-height: 0.95;
    padding-top: 18px;
  }
  .title-small { font-size: 36px; letter-spacing: 1px; }
  .title-big { font-size: 64px; letter-spacing: 1px; margin-top: 4px; }
  .prizes {
    position: absolute;
    left: 190px; top: 495px;
    font-family: "Anton", sans-serif;
    font-size: 38px;
    color: var(--yellow);
    transform: rotate(-6deg);
  }
  .date {
    position: absolute;
    left: 370px; top: 470px;
    transform: rotate(-6deg);
    font-family: "Anton", sans-serif;
    text-transform: uppercase;
    line-height: 0.95;
  }
  .date-day { font-size: 36px; color: var(--white); }
  .date-year { font-size: 78px; color: var(--yellow); }
  .time {
    display: inline-block;
    margin-top: 8px;
    background: var(--magenta);
    border: 3px solid var(--yellow);
    padding: 4px 18px;
    font-size: 24px;
    color: var(--white);
  }
  .seal {
    position: absolute;
    left: 470px; top: 650px;
    width: 96px; height: 96px;
    border-radius: 50%;
    background: #c9a45c;
    border: 5px solid #e6d7a8;
  }
  .details {
    position: absolute;
    left: 40px; top: 612px;
    width: 400px;
    transform: rotate(-6deg);
    font-size: 15px;
    line-height: 1.4;
  }
  .details .label, .details .accent { color: var(--yellow); font-weight: 700; }
  .details .highlight {
    color: var(--yellow);
    font-weight: 800;
    font-size: 24px;
    line-height: 1.15;
  }
  .contact {
    position: absolute;
    left: 320px; top: 758px;
    transform: rotate(-6deg);
    font-size: 14px;
    line-height: 1.4;
  }
  .contact .phone { font-size: 26px; font-weight: 800; color: var(--yellow); }
  .brand {
    position: absolute;
    left: 30px; top: 770px;
    width: 190px; height: 62px;
    background: var(--white);
    border: 3px solid var(--yellow);
    display: flex; align-items: center; justify-content: center;
    color: var(--navy);
    font-weight: 800;
    font-size: 13px;
    text-transform: uppercase;
    text-align: center;
    transform: rotate(-6deg);
  }
</style>
</head>
<body>
  <main class="flyer">
    <svg class="decor" viewBox="0 0 600 850" width="600" height="850">
      <polygon class="photo-panel" role="img" aria-label="Photo of three hands showing rock, paper and scissors gestures" points="80,175 500,120 470,420 130,470" fill="var(--photo-blue)" stroke="var(--magenta)" stroke-width="6"/>
      <polygon points="470,70 540,110 490,150" fill="none" stroke="var(--magenta)" stroke-width="4"/>
      <polygon points="505,40 560,70 520,100" fill="none" stroke="var(--magenta)" stroke-width="3"/>
      <polygon points="150,110 205,140 180,165" fill="var(--cyan)"/>
      <polygon points="95,200 145,185 125,210" fill="var(--yellow)"/>
      <polygon points="500,230 540,205 535,240" fill="var(--yellow)"/>
      <polygon points="40,560 90,520 110,570" fill="none" stroke="var(--magenta)" stroke-width="4"/>
      <polygon points="60,600 110,585 100,610" fill="var(--yellow)"/>
      <polygon points="40,470 100,455 70,480" fill="var(--cyan)"/>
      <circle cx="530" cy="170" r="10" fill="none" stroke="var(--magenta)" stroke-width="3"/>
      <line x1="510" y1="290" x2="600" y2="270" stroke="var(--yellow)" stroke-width="2"/>
      <line x1="20" y1="430" x2="110" y2="415" stroke="var(--yellow)" stroke-width="2"/>
      <line x1="540" y1="130" x2="600" y2="70" stroke="var(--cyan)" stroke-width="2" stroke-dasharray="6 6"/>
      <line x1="90" y1="620" x2="130" y2="560" stroke="var(--cyan)" stroke-width="2" stroke-dasharray="6 6"/>
    </svg>

    <div class="title-box">
      <div class="title-small">Rock, Paper,<br>Scissors</div>
      <div class="title-big">Championship</div>
    </div>
    <div class="prizes">$$$ PRIZES</div>

    <div class="date">
      <div class="date-day">June 9th</div>
      <div class="date-year">2018</div>
      <div class="time">Time: 11am-4pm</div>
    </div>

    <div class="seal" role="img" aria-label="County seal"></div>

    <section class="details">
      <p><span class="label">Fee:</span> $2 to enter, free for spectators</p>
      <p>Heats to determine the overall <span class="accent">‘Rock, Paper, Scissors’</span> champion!</p>
      <p class="highlight">Cash prizes on offer</p>
      <p class="highlight">Live music.</p>
      <p>Food and beverage available for purchase</p>
    </section>

    <section class="contact">
      <p class="phone">908-555-3162</p>
      <p>Belvorrow Sports Center, Calder Falls</p>
      <p>www.belvorrowgrounds.example</p>
    </section>

    <div class="brand">Belvorrow Sports Center</div>
  </main>
</body>
</html>
```